Outdoor mass notification company needing business card design.

Our company name is Harborline Signal Systems Inc located in Amory Mississippi and we sell and maintain "Corvath" Mass Notification Sirens in the US. Outdoor sirens notify people of certain severe dangers such as tornados, severe thunderstorms, flooding, hurricanes and tsunamis. We also serve the oil and gas refining industries to warn of Chemical releases, fires, and lightning alerts.

Contact Information for Business Card

Name, title, cell number, email address

Requirements
Nice to have
• The Corvath logo and also the Tallbrook logo.

```html
<!DOCTYPE html>
<html lang="en">
<head>
<meta charset="utf-8">
<title>Harborline Signal Systems – Business Card</title>
<link rel="stylesheet" href="https://fonts.googleapis.com/css2?family=Crimson+Pro:wght@700&family=Arimo:wght@400;700&display=swap">
<style>
  :root {
    --bg: #2b2b2e;
    --card: #ffffff;
    --navy: #2f4b6c;
    --ink: #1d1d1f;
    --edge: #e6e6e6;
  }
  * { box-sizing: border-box; margin: 0; padding: 0; }
  html, body { width: 1200px; height: 780px; overflow: hidden; }
  body {
    background: var(--bg);
    position: relative;
    font-family: "Arimo", Arial, sans-serif;
  }
  .card {
    position: absolute;
    top: 235px;
    width: 540px;
    height: 310px;
    background: var(--card);
    border-radius: 28px;
    box-shadow: 0 4px 0 var(--edge), 0 8px 0 #d9d9d9, 0 18px 30px rgba(0,0,0,.45);
    overflow: hidden;
  }
  .card--back { left: 40px; }
  .card--front { left: 620px; }

  .wordmark {
    font-family: "Crimson Pro", Georgia, serif;
    font-weight: 700;
    color: var(--navy);
    text-transform: uppercase;
    line-height: 0.95;
  }
  .wordmark span { display: block; }

  .card--front .wordmark {
    position: absolute;
    left: 0; right: 0; top: 108px;
    text-align: center;
    font-size: 44px;
    letter-spacing: 1px;
  }

  .card--back .wordmark {
    position: absolute;
    left: 34px; top: 46px;
    font-size: 23px;
    letter-spacing: 0.5px;
  }
  .card--back .wordmark .line-1 { padding-left: 42px; }

  .divider {
    position: absolute;
    left: 0; top: 0;
    width: 540px; height: 310px;
  }

  .contact {
    position: absolute;
    left: 292px; top: 102px;
    color: var(--ink);
    font-size: 14px;
    line-height: 1.3;
  }
  .contact__name {
    color: var(--navy);
    font-weight: 700;
    font-size: 19px;
    letter-spacing: 0.5px;
    text-transform: uppercase;
  }
  .contact__title { margin-bottom: 8px; }
  .contact__address { margin-bottom: 8px; }
  .contact__list { list-style: none; }
  .contact__list li {
    display: flex;
    align-items: center;
    gap: 6px;
  }
  .contact__list svg { width: 12px; height: 12px; flex: none; }
</style>
</head>
<body>

  <section class="card card--back" aria-label="Business card, contact side">
    <div class="wordmark">
      <span class="line-1">Harborline</span>
      <span class="line-2">Signal Systems</span>
    </div>

    <svg class="divider" viewBox="0 0 540 310" aria-hidden="true">
      <line x1="300" y1="70" x2="210" y2="255" stroke="var(--navy)" stroke-width="2"/>
    </svg>

    <div class="contact">
      <p class="contact__name">Daniel Reyes</p>
      <p class="contact__title">Managing Director</p>
      <p class="contact__address">Your address, City<br>State, Zip 1234</p>
      <ul class="contact__list">
        <li>
          <svg viewBox="0 0 12 12" aria-hidden="true"><path d="M3 1l2 2.5-1 1.2a6 6 0 0 0 3.3 3.3l1.2-1L11 9l-1.2 1.8C6 11 1 6 1.2 2.2z" fill="var(--navy)"/></svg>
          123 456 789
        </li>
        <li>
          <svg viewBox="0 0 12 12" aria-hidden="true"><rect x="1" y="2.5" width="10" height="7" rx="1" fill="var(--navy)"/><path d="M1.5 3l4.5 3.5L10.5 3" stroke="#fff" stroke-width="1" fill="none"/></svg>
          info@yourmail.com
        </li>
        <li>
          <svg viewBox="0 0 12 12" aria-hidden="true"><circle cx="6" cy="6" r="5" fill="var(--navy)"/><path d="M1 6h10M6 1c2 2 2 8 0 10M6 1c-2 2-2 8 0 10" stroke="#fff" stroke-width=".8" fill="none"/></svg>
          www.yourwebsite.com
        </li>
      </ul>
    </div>
  </section>

  <section class="card card--front" aria-label="Business card, logo side">
    <div class="wordmark">
      <span>Harborline</span>
      <span>Signal Systems</span>
    </div>
  </section>

</body>
</html>
```